Real Estate Development Company Web Developer

Hi, I am looking for a website developer to create a website for our new real estate development company. you need to design a website with motion graphics that can be run on any device.
We're looking for sample websites like:
https://larkmontbuild.ca/ or https://www.fennicorehomes.ca/
- The website shall include 6 pages with 1 page hidden.
- The website needs to have 2 versions - English and Chinese
- for your mock-up design, you can use copyright free imagery (we are based in Vancouver, and our projects are townhouses/condos, etc)
Please show examples of professional websites you have done & a mock-up website design for our company. We will shortlist in the next several days and get started straight away. The wording for text content will be detailed in a separate document for each page after we decide the designer.

```html
<!DOCTYPE html>
<html lang="en">
<head>
<meta charset="utf-8">
<title>Halden Properties</title>
<link rel="stylesheet" href="https://fonts.googleapis.com/css2?family=Hind:wght@400;500;600&family=Noto+Serif:wght@700&display=swap">
<style>
:root{
  --white:#ffffff;
  --ink:#3d3d3d;
  --muted:#8a8a8a;
  --brand:#2a6fb3;
  --nav-active:#2a6fb3;
  --story-a:#b77a3e;
  --story-b:#8a3d24;
  --mission-a:#2b90cf;
  --mission-b:#1f6cb0;
  --footer-a:#8f8479;
  --footer-b:#474442;
  --card-shadow:rgba(0,0,0,.22);
}
*{box-sizing:border-box;margin:0;padding:0}
html,body{width:1200px;height:2480px;overflow:hidden;background:var(--white)}
body{position:relative;font-family:"Hind",sans-serif;color:var(--ink)}
.abs{position:absolute}

/* header */
.site-header{left:0;top:0;width:1200px;height:72px;background:var(--white)}
.brand{left:247px;top:18px;font:600 18px/24px "Hind",sans-serif;color:var(--brand);display:flex;align-items:center;gap:7px}
.brand-dot{width:12px;height:12px;background:var(--brand);border-radius:50%}
.main-nav{left:487px;top:23px;display:flex;gap:12px;font-size:9.5px;letter-spacing:.2px}
.main-nav a{color:#333;text-decoration:none}
.main-nav .active{color:var(--nav-active);font-weight:600;margin-right:14px}
.btn-outline{display:flex;align-items:center;justify-content:center;border:1px solid #333;font-size:9.5px;color:#333}
.join-btn{left:787px;top:14px;width:81px;height:29px}
.lang-btn{left:907px;top:14px;width:45px;height:29px;font-size:14px}

/* hero sections */
.story{left:0;top:72px;width:1200px;height:412px;background:linear-gradient(90deg,var(--story-a),var(--story-b))}
.mission{left:0;top:906px;width:1200px;height:520px;background:linear-gradient(90deg,var(--mission-a),var(--mission-b))}
.band-title{position:absolute;left:0;width:1200px;text-align:center;font:700 17px/20px "Noto Serif",serif;color:var(--white);letter-spacing:.3px}
.band-text{position:absolute;left:350px;width:500px;text-align:center;font-size:10.4px;line-height:16.4px;color:var(--white)}
.play-ring{left:560px;top:151px}
.about-btn{left:560px;top:306px;width:82px;height:29px;border:1px solid var(--white);color:var(--white);font-size:9px;display:flex;align-items:center;justify-content:center}

/* testimonial */
.quote-mark{left:0;top:540px;width:1200px;text-align:center;font:700 40px/40px "Noto Serif",serif;color:#555}
.quote-text{left:305px;top:592px;width:590px;text-align:center;font-size:12px;line-height:19.5px;color:#555}
.quote-name{left:0;top:702px;width:1200px;text-align:center;font-size:10.5px;color:#444;letter-spacing:.3px}
.quote-role{left:0;top:720px;width:1200px;text-align:center;font-size:8.5px;color:var(--muted)}
.avatars{left:440px;top:760px}

/* feature cards */
.card{left:301px;width:651px;height:291px;background:var(--white);box-shadow:2px 3px 6px var(--card-shadow)}
.card-photo{left:245px;width:232px;height:187px;background:linear-gradient(180deg,#7fb0e0 0%,#c9d9e8 38%,#6c7f8c 55%,#9a9a96 78%,#8a9a4f 100%)}
.card-title{left:547px;font:700 17px/20px "Noto Serif",serif;color:#444;letter-spacing:.3px}
.card-text{left:547px;width:340px;font-size:10.3px;line-height:16.5px;color:var(--muted)}

/* footer */
.site-footer{left:0;top:2177px;width:1200px;height:303px;background:linear-gradient(100deg,var(--footer-a),var(--footer-b))}
.footer-brand{left:247px;top:2234px;font:600 17px/22px "Hind",sans-serif;color:var(--brand);display:flex;align-items:center;gap:7px}
.footer-about{left:247px;top:2283px;width:225px;font-size:10.5px;line-height:19.5px;color:var(--white)}
.footer-heading{font-size:10.5px;font-weight:600;color:var(--white);letter-spacing:.3px}
.footer-line{font-size:9.8px;line-height:19.2px;color:var(--white)}
.copyright{left:0;top:2413px;width:1200px;text-align:center;font-size:9.8px;color:var(--white)}
</style>
</head>
<body>

<header class="abs site-header">
  <div class="abs brand"><span class="brand-dot"></span>Halden Properties</div>
  <nav class="abs main-nav">
    <a class="active" href="#">HOME</a><a href="#">PROJECTS</a><a href="#">SERVICES</a><a href="#">CONTACT</a>
  </nav>
  <div class="abs btn-outline join-btn">JOIN US</div>
  <div class="abs btn-outline lang-btn">中文</div>
</header>

<section class="abs story" role="img" aria-label="City skyline at the waterfront under a warm copper tint">
  <h2 class="band-title" style="top:109px">OUR STORY</h2>
  <svg class="abs play-ring" width="74" height="74" viewBox="0 0 74 74" aria-hidden="true">
    <circle cx="37" cy="37" r="35" fill="none" stroke="rgba(255,255,255,.3)" stroke-width="2"/>
    <path d="M30 24 L50 37 L30 50 Z" fill="none" stroke="rgba(255,255,255,.3)" stroke-width="2"/>
  </svg>
  <p class="band-text" style="top:142px">This is Photoshop's version&nbsp; of Lorem Ipsum. Proin gravida nibh vel velit auctor aliquet. Aenean sollicitudin, lorem quis bibendum auctor, nisi elit consequat ipsum, nec sagittis sem nibh id elit. Duis sed odio sit amet nibh vulputate cursus</p>
  <p class="band-text" style="top:208px">Morbi accumsan ipsum velit. Nam nec tellus a odio tincidunt auctor a ornare odio. Sed non&nbsp; mauris vitae erat consequat auctor eu in elit. Class aptent taciti sociosqu ad litora torquent per conubia nostra, per inceptos himenaeos.</p>
  <div class="abs about-btn">ABOUT US</div>
</section>

<section class="testimonial">
  <div class="abs quote-mark">&ldquo;</div>
  <p class="abs quote-text">This is Photoshop's version&nbsp; of Lorem Ipsum. Proin gravida nibh vel velit auctor aliquet. Aenean sollicitudin, lorem quis bibendum auctor, nisi elit consequat ipsum, nec sagittis sem nibh id elit. Duis sed odio sit amet nibh vulputate cursus a sit amet mauris. Morbi accumsan ipsum velit. Nam nec tellus a odio tincidunt auctor a ornare odio. Sed non&nbsp; mauris vitae erat consequat auctor eu in elit.</p>
  <div class="abs quote-name">MARA ELLISON</div>
  <div class="abs quote-role">CEO NORTHWOOD</div>
  <svg class="abs avatars" width="320" height="60" viewBox="0 0 320 60" aria-hidden="true">
    <path d="M21 22 L15 30 L21 38" fill="none" stroke="#777" stroke-width="1.3"/>
    <path d="M299 22 L305 30 L299 38" fill="none" stroke="#777" stroke-width="1.3"/>
    <circle cx="62" cy="30" r="17" fill="#c9a58a"><title>Client portrait</title></circle>
    <circle cx="106" cy="30" r="17" fill="#7a5a3e"><title>Client portrait</title></circle>
    <circle cx="160" cy="30" r="26" fill="#b98a84"><title>Client portrait</title></circle>
    <circle cx="213" cy="30" r="17" fill="#c08f74"><title>Client portrait</title></circle>
    <circle cx="257" cy="30" r="17" fill="#5f6166"><title>Client portrait</title></circle>
  </svg>
</section>

<section class="abs mission" role="img" aria-label="High-rise residential towers under a blue tint">
  <h2 class="band-title" style="top:151px">OUR MISSION</h2>
  <p class="band-text" style="top:184px">This is Photoshop's version&nbsp; of Lorem Ipsum. Proin gravida nibh vel velit auctor aliquet. Aenean sollicitudin, lorem quis bibendum auctor, nisi elit consequat ipsum, nec sagittis sem nibh id elit. Duis sed odio sit amet nibh vulputate cursus</p>
  <p class="band-text" style="top:250px">Morbi accumsan ipsum velit. Nam nec tellus a odio tincidunt auctor a ornare odio. Sed non&nbsp; mauris vitae erat consequat auctor eu in elit. Class aptent taciti sociosqu ad litora torquent per conubia nostra, per inceptos himenaeos.</p>
</section>

<article>
  <div class="abs card" style="top:1491px"></div>
  <div class="abs card-photo" style="top:1536px" role="img" aria-label="Modern glass office building with parking lot under blue sky"></div>
  <h3 class="abs card-title" style="top:1535px">LOREM IPSUM</h3>
  <p class="abs card-text" style="top:1580px">This is Photoshop's version&nbsp; of Lorem Ipsum. Proin gravida nibh vel velit auctor aliquet. Aenean sollicitudin, lorem quis bibendum auctor, nisi elit consequat ipsum, nec sagittis sem nibh id elit. Duis sed odio sit amet nibh vulputate cursus</p>
  <p class="abs card-text" style="top:1663px">Morbi accumsan ipsum velit. Nam nec tellus a odio tincidunt auctor a ornare odio. Sed non&nbsp; mauris vitae erat consequat auctor eu in elit. Class aptent taciti sociosqu ad litora torquent per conubia nostra, per inceptos himenaeos.</p>
</article>

<article>
  <div class="abs card" style="top:1820px"></div>
  <div class="abs card-photo" style="top:1868px" role="img" aria-label="Modern glass office building with parking lot under blue sky"></div>
  <h3 class="abs card-title" style="top:1865px">LOREM IPSUM</h3>
  <p class="abs card-text" style="top:1910px">This is Photoshop's version&nbsp; of Lorem Ipsum. Proin gravida nibh vel velit auctor aliquet. Aenean sollicitudin, lorem quis bibendum auctor, nisi elit consequat ipsum, nec sagittis sem nibh id elit. Duis sed odio sit amet nibh vulputate cursus</p>
  <p class="abs card-text" style="top:1993px">Morbi accumsan ipsum velit. Nam nec tellus a odio tincidunt auctor a ornare odio. Sed non&nbsp; mauris vitae erat consequat auctor eu in elit. Class aptent taciti sociosqu ad litora torquent per conubia nostra, per inceptos himenaeos.</p>
</article>

<footer class="abs site-footer"></footer>
<div class="abs footer-brand"><span class="brand-dot"></span>Halden Properties</div>
<p class="abs footer-about">lorem quis bibendum auctor, nisi elit consequat ipsum, nec sagittis sem nibh elit. Duis sed odio sit amet auctror a ornare odio non mauris vitae erat in elit</p>

<div class="abs footer-heading" style="left:487px;top:2244px">OUR STUDIO</div>
<svg class="abs" style="left:487px;top:2282px" width="14" height="14" viewBox="0 0 14 14" aria-hidden="true">
  <path d="M7 13 C3 8.5 2 6.5 2 5 A5 5 0 0 1 12 5 C12 6.5 11 8.5 7 13 Z" fill="none" stroke="#fff" stroke-width="1"/>
  <circle cx="7" cy="5" r="1.8" fill="none" stroke="#fff" stroke-width="1"/>
</svg>
<p class="abs footer-line" style="left:509px;top:2280px;width:200px">Lorem Ipsum, Lorem Ipsum Ipsum No.12 -<br>11, Lorem - Vancouver<br>11100 - Lorem</p>
<svg class="abs" style="left:487px;top:2351px" width="14" height="14" viewBox="0 0 14 14" aria-hidden="true">
  <path d="M3 2 L5 2 L6 5 L4.5 6 C5.5 8 6 8.5 8 9.5 L9 8 L12 9 L12 11 C12 12 11 12.5 10 12.5 C6 12 2 8 1.5 4 C1.5 3 2 2 3 2 Z" fill="none" stroke="#fff" stroke-width="1"/>
</svg>
<p class="abs footer-line" style="left:509px;top:2347px">(+00) 00-0000- 0000</p>

<div class="abs footer-heading" style="left:734px;top:2244px;font-weight:500">FOLLOW US</div>
<svg class="abs" style="left:732px;top:2274px" width="130" height="30" viewBox="0 0 130 30" aria-hidden="true">
  <g fill="none" stroke="#fff" stroke-width="1">
    <circle cx="15" cy="15" r="13"/><circle cx="47" cy="15" r="13"/><circle cx="79" cy="15" r="13"/><circle cx="112" cy="15" r="13"/>
  </g>
</svg>

<div class="abs copyright">Copyright © 2022 - Halden Properties</div>

</body>
</html>
```